I need the front of this bottle designed for and calendula and tallow lotion. the dimenstions are 236mm by 84 mm the Minimalists design if you choose a graphic should be very minimal and high end I don thave a logo. My company name is The Bright Seed Co, If you want to ceate a logo using the TBSC ( letters only) That would be ok

```html
<!DOCTYPE html>
<html lang="en">
<head>
<meta charset="utf-8">
<title>The Bright Seed Co. – Calendula and Tallow Lotion Label</title>
<link rel="stylesheet" href="https://fonts.googleapis.com/css2?family=Poppins:wght@300;400;600&family=Questrial&display=swap">
<style>
  :root {
    --paper: #ffffff;
    --ink: #231f20;
  }
  * { margin: 0; padding: 0; box-sizing: border-box; }
  html, body {
    width: 1200px;
    height: 1200px;
    overflow: hidden;
    background: var(--paper);
  }
  .label {
    position: relative;
    width: 1200px;
    height: 1200px;
    color: var(--ink);
    text-align: center;
  }
  .label > * {
    position: absolute;
    left: 0;
    right: 0;
  }
  .brand {
    top: 148px;
    font-family: "Poppins", sans-serif;
    font-weight: 400;
    font-size: 26px;
    line-height: 26px;
    letter-spacing: 0.3em;
    padding-left: 0.3em;
  }
  .rule {
    left: 50%;
    width: 109px;
    height: 3px;
    margin-left: -54.5px;
    background: var(--ink);
  }
  .rule--top { top: 184px; }
  .rule--bottom { top: 1016px; }
  .product-name {
    top: 282px;
    font-family: "Questrial", sans-serif;
    font-weight: 400;
    font-size: 86px;
    line-height: 83px;
  }
  .product-type {
    top: 560px;
    font-family: "Poppins", sans-serif;
    font-weight: 300;
    font-size: 36px;
    line-height: 36px;
  }
  .net-volume {
    top: 1036px;
    font-family: "Poppins", sans-serif;
    font-weight: 600;
    font-size: 22px;
    line-height: 22px;
    letter-spacing: 0.22em;
    padding-left: 0.22em;
  }
</style>
</head>
<body>
  <main class="label">
    <p class="brand">The Bright Seed Co.</p>
    <div class="rule rule--top"></div>
    <h1 class="product-name">Calendula<br>and<br>Tallow</h1>
    <p class="product-type">Lotion</p>
    <div class="rule rule--bottom"></div>
    <p class="net-volume">Net:500 ml</p>
  </main>
</body>
</html>
```